PowerPoint Template Needed for Investment Firm

Norvelle Capital Management is an emerging wealth management firm based in New Jersey. It offers superior investment returns to high net worth individuals and institutions by finding undervalued assets.

We recently selected a company logo which was inspired by the Tucana constellation. Beta Tucanae is a group of six stars, containing star cluster 47 Tucanae, rated the second brightest object in the sky.

Now we need a PowerPoint template with the designs for the following:

1. Title/cover page slide
2. Content slide with title
3. Section slide - to introduce a new section
4. Final slide - with contact information

The slides will be used at investor presentations, that is, to provide information about the company to potential investors. Since we are an investment firm, the design should project a sense of stability, growth and professionalism. The owner is interested in something simple yet striking, which of course is consistent with the logo. I'm thinking more conservative colors and Sans Serif fonts.

I plan on changing the status to non-refundable once I see some designs that I really like.

Target Market(s)

Wealthy individuals, probably middle aged or older, in the US

Industry/Entity Type

Conservative

Requirements
Must have
• Sans serif fonts
Clean, very professional look
Conservative colors that complement existing logo
Should not have
• Anything too busy or complicated

```html
<!DOCTYPE html>
<html lang="en">
<head>
<meta charset="utf-8">
<title>Norvelle Capital Management – Slide Templates</title>
<link rel="stylesheet" href="https://fonts.googleapis.com/css2?family=Open+Sans:wght@400;700&display=swap">
<style>
  :root {
    --page: #ffffff;
    --slide: #e5e6e8;
    --charcoal: #3a3839;
    --slate-blue: #3d5096;
    --royal-blue: #1341ad;
    --glow-blue: #1545b8;
    --band-edge: #26272b;
    --mark-blue: #1f3aa0;
    --name-ink: #3c3c3f;
    --text-light: #dfe4f2;
    --text-dark: #3a3a3c;
  }
  * { margin: 0; padding: 0; box-sizing: border-box; }
  html, body {
    width: 1200px; height: 938px; overflow: hidden;
    background: var(--page);
    font-family: "Open Sans", Arial, sans-serif;
  }
  .sheet { position: relative; width: 1200px; height: 938px; }
  .slide {
    position: absolute; width: 578px; height: 448px;
    background: var(--slide); overflow: hidden;
  }
  .slide--cover   { left: 18px;  top: 18px; }
  .slide--content { left: 605px; top: 18px; }
  .slide--section { left: 18px;  top: 473px; }
  .slide--closing { left: 605px; top: 473px; }

  .band { position: absolute; left: 0; right: 0; top: 366px; height: 82px; }
  .band--gradient {
    background: radial-gradient(ellipse 60% 140% at 50% 50%, var(--glow-blue) 0%, #163a8c 35%, var(--band-edge) 100%);
  }
  .band--charcoal { background: var(--charcoal); }
  .band__fill { position: absolute; left: 155px; right: 0; top: 0; bottom: 0; }
  .band__fill--slate { background: var(--slate-blue); }
  .band__fill--royal { background: var(--royal-blue); }
  .band__url {
    position: absolute; left: 13px; top: 62px;
    font-size: 9px; line-height: 12px; color: var(--text-light);
  }

  .side-column {
    position: absolute; left: 0; top: 0; width: 155px; height: 366px;
    background: var(--charcoal);
  }

  .brand {
    position: absolute; display: flex; flex-direction: column; align-items: center;
    color: var(--name-ink); font-weight: 700;
  }
  .brand__mark { width: 48px; height: 48px; border-radius: 6px; background: var(--mark-blue); }
  .brand__name {
    display: flex; flex-direction: column; align-items: center;
    margin-top: 3px; text-align: center; white-space: nowrap;
  }
  .brand__word {
    font-size: 16px; line-height: 18px; letter-spacing: 3px;
    text-transform: uppercase; margin-right: -3px;
  }
  .brand__sub { font-size: 8.5px; line-height: 10px; }

  .slide--cover .brand { left: 18px; width: 120px; top: 275px; }

  .band .brand { left: 0; width: 155px; top: 9px; }
  .band .brand__mark { width: 37px; height: 37px; border-radius: 5px; }
  .band .brand__name { margin-top: 2px; }
  .band .brand__word { font-size: 12.5px; line-height: 14px; letter-spacing: 2.5px; margin-right: -2.5px; }
  .band .brand__sub { font-size: 7.5px; line-height: 9px; }

  .contact-line {
    position: absolute; left: 0; right: 0; top: 343px; text-align: center;
    font-size: 9.5px; line-height: 12px; color: var(--text-dark);
  }
</style>
</head>
<body>
<main class="sheet">
  <section class="slide slide--cover" aria-label="Title slide">
    <div class="brand">
      <div class="brand__mark"></div>
      <div class="brand__name"><span class="brand__word">Norvelle</span><span class="brand__sub">Capital Management</span></div>
    </div>
    <div class="band band--gradient"></div>
  </section>

  <section class="slide slide--content" aria-label="Content slide">
    <div class="band">
      <div class="brand">
        <div class="brand__mark"></div>
        <div class="brand__name"><span class="brand__word">Norvelle</span><span class="brand__sub">Capital Management</span></div>
      </div>
      <div class="band__fill band__fill--slate">
        <span class="band__url">www.norvellecapmgmt.com</span>
      </div>
    </div>
  </section>

  <section class="slide slide--section" aria-label="Section slide">
    <div class="side-column"></div>
    <div class="band">
      <div class="brand">
        <div class="brand__mark"></div>
        <div class="brand__name"><span class="brand__word">Norvelle</span><span class="brand__sub">Capital Management</span></div>
      </div>
      <div class="band__fill band__fill--royal">
        <span class="band__url">www.norvellecapmgmt.com</span>
      </div>
    </div>
  </section>

  <section class="slide slide--closing" aria-label="Contact slide">
    <p class="contact-line">48 Harbor St. Newark, NJ 07102 | www.norvellecapmgmt.com | mhale@norvellecapmgmt.com</p>
    <div class="band band--charcoal"></div>
  </section>
</main>
</body>
</html>
```